Lanternfield Systems Bi Fold Brocher

I need a bi fold (front/back page 1 & front/back page 2) color brochure designed to pass out to clients at a convention. My website is lanternfieldsys.example. Please take images and text from the website to create the brochure. Use the products and product descriptions to display what we offer. Use the text and quotes to describe what we do. Make it professional, descriptive, and full of useful information.

Industry/Entity Type

Business Software

Font styles to use
Serif

Colors
00a990
33b8a4
86cfc6
fbf289
0255a3
3377b5
85acd3

Requirements
Must have
• Contact Info:
• Address:
• 728 Mossgate Boulevard
• Building 200, Suite 1187
• Aldermoor, ST 30987
• Telephone: 1 (555) 274.8816
• Toll Free: 1 (800) 555.0147
• Email: contact@lanternfieldsys.example
Nice to have
• Good backrounds

```html
<!DOCTYPE html>
<html lang="en">
<head>
<meta charset="UTF-8">
<title>Lanternfield Systems – Software Features</title>
<link href="https://fonts.googleapis.com/css2?family=Cabin:ital,wght@0,400;0,500;0,600;1,600;1,700&display=swap" rel="stylesheet">
<style>
  :root {
    --canvas: #b9b9b9;
    --paper: #f1f1f1;
    --paper-shade: #e4e6e6;
    --swoosh: #dde3e3;
    --heading: #6e7072;
    --body-text: #3b4246;
    --teal: #33b8a4;
    --teal-dark: #00a990;
    --blue: #0a4a9a;
    --ink: #1f2a33;
  }
  * { margin: 0; padding: 0; box-sizing: border-box; }
  html, body { width: 1200px; height: 900px; overflow: hidden; }
  body {
    background: var(--canvas);
    font-family: "Cabin", sans-serif;
    position: relative;
  }
  .page {
    position: absolute;
    left: 256px; top: 0;
    width: 688px; height: 900px;
    background: linear-gradient(160deg, #f7f7f7 0%, var(--paper) 55%, var(--paper-shade) 100%);
    overflow: hidden;
  }
  .swoosh { position: absolute; left: 0; top: 0; width: 688px; height: 475px; }
  .features-title {
    position: absolute; left: 67px; top: 68px;
    color: var(--heading);
    font-style: italic; font-weight: 600;
    line-height: 1;
  }
  .features-title .kicker { display: block; font-size: 18px; letter-spacing: 0.5px; }
  .features-title .main { display: block; font-size: 27px; font-weight: 700; letter-spacing: 0.5px; margin-top: 2px; }
  .feature-list {
    position: absolute; left: 64px; top: 139px; width: 567px;
    list-style: none;
  }
  .feature {
    display: flex; gap: 17px;
    margin-bottom: 18px;
  }
  .feature-icon { flex: 0 0 17px; width: 17px; height: 20px; margin-top: 1px; }
  .feature-text {
    font-size: 13.2px; line-height: 18.2px;
    letter-spacing: 0.15px;
    color: var(--body-text);
    text-align: justify;
  }
  .photo-band {
    position: absolute; left: 0; top: 475px; width: 630px; height: 166px;
    background: linear-gradient(180deg, #c9c2ad 0%, #b7a889 45%, #8d7a52 75%, #5d5038 100%);
  }
  .accent-band {
    position: absolute; left: 630px; top: 475px; width: 58px; height: 166px;
    background: var(--blue);
  }
  .brand {
    position: absolute; left: 0; top: 708px; width: 688px;
    display: flex; justify-content: center; align-items: center; gap: 10px;
  }
  .brand-dot { width: 22px; height: 22px; border-radius: 50%; background: var(--teal-dark); }
  .brand-name { font-size: 28px; font-weight: 600; color: var(--ink); }
  .contact {
    position: absolute; left: 0; top: 763px; width: 688px;
    text-align: center; color: var(--ink);
    font-size: 10.5px; line-height: 15px; font-style: normal;
  }
  .contact .gap { margin-top: 6px; }
  .contact span + span { margin-left: 12px; }
</style>
</head>
<body>
  <main class="page">
    <svg class="swoosh" viewBox="0 0 688 475" aria-hidden="true">
      <path d="M20 475 C 180 300, 420 110, 688 50 L688 475 Z" fill="var(--swoosh)" opacity="0.85"/>
    </svg>

    <h1 class="features-title">
      <span class="kicker">SOFTWARE</span>
      <span class="main">FEATURES</span>
    </h1>

    <ul class="feature-list">
      <li class="feature">
        <svg class="feature-icon" viewBox="0 0 17 20" aria-hidden="true"><rect x="2" y="1" width="13" height="13" rx="3" fill="none" stroke="var(--teal)" stroke-width="1.8"/><rect x="4" y="4" width="9" height="4" fill="var(--teal)"/><circle cx="5.5" cy="11" r="1.1" fill="var(--teal)"/><circle cx="11.5" cy="11" r="1.1" fill="var(--teal)"/><path d="M5 15 L2 19 M12 15 L15 19" stroke="var(--teal)" stroke-width="1.8"/></svg>
        <p class="feature-text">Know where every rail car is all the time. Managing rail car locations within your terminal becomes simple and fast using our web-based or tablet application.</p>
      </li>
      <li class="feature">
        <svg class="feature-icon" viewBox="0 0 17 20" aria-hidden="true"><rect x="2" y="1" width="13" height="13" rx="3" fill="none" stroke="var(--teal)" stroke-width="1.8"/><rect x="4" y="4" width="9" height="4" fill="var(--teal)"/><circle cx="5.5" cy="11" r="1.1" fill="var(--teal)"/><circle cx="11.5" cy="11" r="1.1" fill="var(--teal)"/><path d="M5 15 L2 19 M12 15 L15 19" stroke="var(--teal)" stroke-width="1.8"/></svg>
        <p class="feature-text">Manage rail transloading activities to and from a truck or vessel. The software allows the transload terminal operation to effectively and efficiently manage each transaction, decrease paper processing, and provide customers with live inventory and access to transactions.</p>
      </li>
      <li class="feature">
        <svg class="feature-icon" viewBox="0 0 17 20" aria-hidden="true"><rect x="2" y="1" width="13" height="13" rx="3" fill="none" stroke="var(--teal)" stroke-width="1.8"/><rect x="4" y="4" width="9" height="4" fill="var(--teal)"/><circle cx="5.5" cy="11" r="1.1" fill="var(--teal)"/><circle cx="11.5" cy="11" r="1.1" fill="var(--teal)"/><path d="M5 15 L2 19 M12 15 L15 19" stroke="var(--teal)" stroke-width="1.8"/></svg>
        <p class="feature-text">Built-in demurrage management functionality that maintains key data to track and respond to demurrage challenges.</p>
      </li>
      <li class="feature">
        <svg class="feature-icon" viewBox="0 0 17 20" aria-hidden="true"><rect x="2" y="1" width="13" height="13" rx="3" fill="none" stroke="var(--teal)" stroke-width="1.8"/><rect x="4" y="4" width="9" height="4" fill="var(--teal)"/><circle cx="5.5" cy="11" r="1.1" fill="var(--teal)"/><circle cx="11.5" cy="11" r="1.1" fill="var(--teal)"/><path d="M5 15 L2 19 M12 15 L15 19" stroke="var(--teal)" stroke-width="1.8"/></svg>
        <p class="feature-text">Automated railcar inspections are now affordable and reliable. You can create unlimited inspection forms and assign specific inspections to individual users. No more paper, no more going back for photos, and no more sorting through the daily inspection sheets.</p>
      </li>
      <li class="feature">
        <svg class="feature-icon" viewBox="0 0 17 20" aria-hidden="true"><rect x="2" y="1" width="13" height="13" rx="3" fill="none" stroke="var(--teal)" stroke-width="1.8"/><rect x="4" y="4" width="9" height="4" fill="var(--teal)"/><circle cx="5.5" cy="11" r="1.1" fill="var(--teal)"/><circle cx="11.5" cy="11" r="1.1" fill="var(--teal)"/><path d="M5 15 L2 19 M12 15 L15 19" stroke="var(--teal)" stroke-width="1.8"/></svg>
        <p class="feature-text">Lanternfield Systems has built a robust system for handling and generating EDI messages in order to automate data entry and communicate key pieces of data with the carrier.</p>
      </li>
    </ul>

    <div class="photo-band" role="img" aria-label="Photograph of a freight locomotive on rail tracks in an industrial yard at golden hour"></div>
    <div class="accent-band"></div>

    <div class="brand">
      <span class="brand-dot"></span>
      <span class="brand-name">Lanternfield Systems</span>
    </div>

    <address class="contact">
      <div>728 Mossgate Boulevard,&nbsp; Building 200, Suite 1187</div>
      <div>Aldermoor, ST 30987</div>
      <div class="gap"><span>Telephone: 1 (555) 274.8816</span><span>Toll Free: 1 (800) 555.0147</span></div>
      <div>Email: contact@lanternfieldsys.example</div>
      <div>www.lanternfieldsys.example</div>
    </address>
  </main>
</body>
</html>
```